Lirevo Nocturna

Website for a night club with live music and cabaret dancers. I would like to have the following Menu: 1.) Home; 2) The Facilities; 3) The Show; 4) Other Attractions; 5) Videos & Fotos; 6) Program; 7) Reservations; 8) Membership; 9) Contacts.

The pages should be easily editable and allow to enter text, including the menu since the final version will be in both English and Portuguese. It should have a toggle or links for the Portuguese language and the English Language.

The night club itself is called "LIREVO NOCTURNA"; and its URL is www.lirevonocturna.example.

Industry/Entity Type

Night Club

```html
<!DOCTYPE html>
<html lang="en">
<head>
<meta charset="utf-8">
<title>Lirevo Nocturna</title>
<link rel="stylesheet" href="https://fonts.googleapis.com/css2?family=Roboto:wght@400;500&family=Open+Sans:wght@400;600&display=swap">
<style>
:root{
  --page:#1b1b1b;
  --page-hi:#262626;
  --red:#e8473b;
  --yellow:#fdc500;
  --gold:#c79a00;
  --white:#ffffff;
  --panel:#4a4a4a;
  --dark:#1c1c1c;
  --footer:#3b3b3b;
  --text-dark:#333333;
  --text-light:#e9e9e9;
}
*{box-sizing:border-box;margin:0;padding:0}
html,body{width:1077px;height:1200px;overflow:hidden}
body{position:relative;background:linear-gradient(160deg,var(--page-hi),var(--page) 60%);font-family:"Open Sans",sans-serif;color:var(--text-light)}
.brand{position:absolute;left:160px;top:44px;font-family:"Roboto",sans-serif;font-weight:500;font-size:29px;letter-spacing:1px;color:var(--yellow)}
.lang{position:absolute;left:839px;top:29px;width:82px;height:24px;border:1px solid #bbb;border-radius:3px;font-family:"Roboto",sans-serif;font-size:10px;color:#fff;display:flex;align-items:center;gap:4px;padding-left:5px}
.lang .flag{width:15px;height:10px;background:#b22234}
.phone{position:absolute;left:765px;top:62px;display:flex;align-items:center;gap:9px;font-family:"Roboto",sans-serif;font-size:21px;color:#fff}
.nav{position:absolute;left:158px;top:109px;width:764px;height:49px;background:var(--red);display:flex;align-items:center;font-family:"Roboto",sans-serif;font-size:11.4px;color:#fff}
.nav a{color:inherit;text-decoration:none;padding:0 8px;height:100%;display:flex;align-items:center}
.nav a.current{background:var(--yellow);padding:0 11px}
.hero{position:absolute;left:158px;top:158px;width:764px;height:364px;background:linear-gradient(180deg,#7a8a3a 0%,#b7a04a 25%,#8a5a4a 55%,#4a3a3a 100%)}
.caption{position:absolute;left:0;bottom:0;width:522px;height:68px;background:rgba(20,20,20,.75);padding:17px 0 0 30px;font-family:"Roboto",sans-serif;color:#fff}
.caption h1{font-weight:400;font-size:14.5px}
.caption p{font-size:14px;margin-top:8px;padding-left:3px}
.arrows{position:absolute;left:524px;bottom:0;width:27px}
.arrows span{display:flex;height:34px;background:var(--yellow);align-items:center;justify-content:center}
.arrows span+span{border-top:1px solid #c79a00}
.features{position:absolute;left:158px;top:550px;width:764px;height:302px;background:var(--panel)}
.card{position:absolute;top:28px;width:228px;height:240px;background:#f7f7f7;box-shadow:0 1px 3px rgba(0,0,0,.4)}
.card .img{height:146px;border-bottom:3px solid var(--yellow)}
.card h2{font-family:"Roboto",sans-serif;font-weight:400;font-size:14px;color:var(--red);margin:10px 0 0 15px}
.card p{font-size:10.5px;line-height:17px;color:var(--text-dark);margin:5px 10px 0 16px}
.card .more{position:absolute;right:10px;bottom:12px}
.welcome{position:absolute;left:158px;top:854px;width:764px;height:252px;background:var(--dark)}
.welcome h2{position:absolute;left:25px;top:29px;font-family:"Roboto",sans-serif;font-weight:400;font-size:16px;color:var(--yellow)}
.welcome p{position:absolute;left:24px;top:56px;width:378px;font-size:10.5px;line-height:20px;text-align:justify}
.btn{position:absolute;left:24px;top:190px;height:22px;display:flex;font-family:"Roboto",sans-serif;font-size:9.5px;color:#222}
.btn span{background:var(--yellow);padding:0 7px;display:flex;align-items:center}
.btn i{width:19px;background:var(--gold);display:flex;align-items:center;justify-content:center}
.video{position:absolute;left:422px;top:20px;width:320px;height:194px;background:#fff;padding:6px}
.video .screen{position:relative;height:100%;border-radius:5px;background:linear-gradient(180deg,#3a3530,#5a4030 45%,#2a2522);overflow:hidden}
.video .bar{position:absolute;left:0;right:0;bottom:0;height:24px;background:#1a1a1a;display:flex;align-items:center;gap:7px;padding:0 8px;font-size:7px;color:#ddd}
.footer{position:absolute;left:156px;top:1107px;width:766px;height:93px;background:var(--footer)}
.contact{position:absolute;left:25px;top:34px;display:flex;gap:8px;align-items:center;font-size:11px;line-height:17px;color:#fff}
.social{position:absolute;left:314px;top:36px;display:flex;gap:8px}
.social span{width:30px;height:29px;border-radius:2px}
.copy{position:absolute;left:586px;top:50px;font-size:11px;color:#fff}
</style>
</head>
<body>
<header>
  <div class="brand">LIREVO NOCTURNA</div>
  <div class="lang"><span class="flag"></span>ENGLISH ⌄</div>
  <div class="phone">
    <svg width="20" height="20" viewBox="0 0 20 20"><circle cx="10" cy="10" r="8.5" fill="none" stroke="#fdc500" stroke-width="1.6"/><path d="M7 5.5l1.5 2.5-1 1.2c.6 1.4 1.6 2.4 3 3l1.2-1 2.5 1.5-.8 1.8c-3.8-.3-7-3.5-7.3-7.3z" fill="#fdc500"/></svg>
    555-014-2736
  </div>
  <nav class="nav">
    <a class="current">HOME</a><a>THE FACILITIES</a><a>THE SHOW</a><a>OTHER ATTRACTIONS</a><a>VIDEOS &amp; FOTOS</a><a>PROGRAM</a><a>RESERVATIONS</a><a>MEMBERSHIP</a><a>CONTACTS</a>
  </nav>
</header>

<section class="hero" role="img" aria-label="Four cabaret dancers in colourful feathered costumes and headdresses">
  <div class="caption">
    <h1>WE ARE NIGHT CLUB WITH LIVE MUSIC AND CABARET DANCERS</h1>
    <p>Ipsum is simply dummy text of the printing and typesetting industry</p>
  </div>
  <div class="arrows">
    <span><svg width="12" height="20" viewBox="0 0 12 20"><path d="M2 2l8 8-8 8" fill="none" stroke="#fff" stroke-width="2"/></svg></span>
    <span><svg width="12" height="20" viewBox="0 0 12 20"><path d="M10 2l-8 8 8 8" fill="none" stroke="#fff" stroke-width="2"/></svg></span>
  </div>
</section>

<section class="features">
  <article class="card" style="left:23px">
    <div class="img" role="img" aria-label="Club building exterior with glass facade and palm trees" style="background:linear-gradient(180deg,#8b98a5,#4f5e5a 60%,#2a302a)"></div>
    <h2>OTHER ATTRACTIONS</h2>
    <p>Lorem Ipsum is simply dummy text of the printing and typesetting industry</p>
    <svg class="more" width="14" height="12" viewBox="0 0 14 12"><path d="M1 1l5 5-5 5M7 1l5 5-5 5" fill="none" stroke="#c79a00" stroke-width="1.8"/></svg>
  </article>
  <article class="card" style="left:268px">
    <div class="img" role="img" aria-label="Dancers in red and yellow costumes performing on stage with drums" style="background:linear-gradient(180deg,#3a3f5a,#8a4a3a 55%,#c8a070)"></div>
    <h2>THE SHOW</h2>
    <p>Lorem Ipsum is simply dummy text of the printing and typesetting industry</p>
    <svg class="more" width="14" height="12" viewBox="0 0 14 12"><path d="M1 1l5 5-5 5M7 1l5 5-5 5" fill="none" stroke="#c79a00" stroke-width="1.8"/></svg>
  </article>
  <article class="card" style="left:513px">
    <div class="img" role="img" aria-label="Dance floor lit with colourful club lights" style="background:linear-gradient(180deg,#5a1414,#8a2a4a 55%,#7a3aa8)"></div>
    <h2>RESERVATIONS</h2>
    <p>Lorem Ipsum is simply dummy text of the printing and typesetting industry</p>
    <svg class="more" width="14" height="12" viewBox="0 0 14 12"><path d="M1 1l5 5-5 5M7 1l5 5-5 5" fill="none" stroke="#c79a00" stroke-width="1.8"/></svg>
  </article>
</section>

<section class="welcome">
  <h2>WELCOME TO LIREVO NOCTURNA</h2>
  <p>Lorem Ipsum has been the industry's standard dummy text ever since the 1500s, when an unknown printer took a galley of type and scrambled it to make a type specimen book. It has survived not only five centuries, but also the leap into electronic typesetting, remaining essentially unchanged. It was popularised in the 1960s with the release of Letraset sheets containing Lorem Ipsum passages, and more recently with desktop publishing software</p>
  <a class="btn"><span>READ MORE</span><i><svg width="8" height="12" viewBox="0 0 8 12"><path d="M1 1l5 5-5 5" fill="none" stroke="#fff" stroke-width="1.5"/></svg></i></a>
  <div class="video">
    <div class="screen" role="img" aria-label="Video of the club interior with bar and lounge seating">
      <svg style="position:absolute;left:135px;top:68px" width="40" height="40" viewBox="0 0 40 40"><circle cx="20" cy="20" r="19" fill="rgba(0,0,0,.45)"/><path d="M15 11l13 9-13 9z" fill="#fff"/></svg>
      <div class="bar">
        <svg width="11" height="11" viewBox="0 0 11 11"><circle cx="5.5" cy="5.5" r="4.5" fill="none" stroke="#fff"/><path d="M4.3 3.5l3 2-3 2z" fill="#fff"/></svg>
        <svg width="30" height="8" viewBox="0 0 30 8"><path d="M0 3h2l3-3v8L2 5H0z" fill="#e8473b"/><path d="M13 1v6M16 1v6M19 1v6M22 1v6M25 1v6" stroke="#e8473b" stroke-width="1.2"/></svg>
        <svg width="135" height="4" viewBox="0 0 135 4"><rect width="135" height="3" y=".5" fill="#555"/><rect width="48" height="3" y=".5" fill="#e8473b"/></svg>
        <span>01:30 / 04:55</span>
        <svg width="9" height="8" viewBox="0 0 9 8"><rect x=".5" y=".5" width="8" height="7" fill="none" stroke="#fff"/></svg>
        <svg width="8" height="8" viewBox="0 0 8 8"><circle cx="4" cy="4" r="3" fill="none" stroke="#fff" stroke-width="1.5"/></svg>
      </div>
    </div>
  </div>
</section>

<footer class="footer">
  <div class="contact">
    <svg width="21" height="21" viewBox="0 0 20 20"><circle cx="10" cy="10" r="8.5" fill="none" stroke="#fff" stroke-width="1.4"/><path d="M7 5.5l1.5 2.5-1 1.2c.6 1.4 1.6 2.4 3 3l1.2-1 2.5 1.5-.8 1.8c-3.8-.3-7-3.5-7.3-7.3z" fill="#fff"/></svg>
    <div>Email: info@lirevonocturna.example<br>Phone: 555-014-2736</div>
  </div>
  <div class="social">
    <span style="background:#2fa9dc"></span>
    <span style="background:#d8352a"></span>
    <span style="background:#3a5793"></span>
    <span style="background:#1e7bb8"></span>
  </div>
  <div class="copy">Copyright © 2014 All Rights</div>
</footer>
</body>
</html>
```